KRT Design Business Card

I need to develop a business card for my real estate design and investment company. Something clean, classic and professional with a modern vibe.

Industry/Entity Type

Real Estate

Font styles to use
Serif
Sans Serif

```html
<!DOCTYPE html>
<html lang="en">
<head>
<meta charset="utf-8">
<title>KRT Design Business Card</title>
<link href="https://fonts.googleapis.com/css2?family=Didact+Gothic&display=swap" rel="stylesheet">
<style>
  :root {
    --backdrop: #3a1210;
    --card: #ffffff;
    --ink: #2b2b2b;
    --ink-soft: #3c3c3c;
    --shadow: rgba(0, 0, 0, 0.45);
  }
  * { margin: 0; padding: 0; box-sizing: border-box; }
  html, body {
    width: 1200px;
    height: 1000px;
    overflow: hidden;
    background: var(--backdrop);
    font-family: "Didact Gothic", "Century Gothic", sans-serif;
    color: var(--ink);
  }
  .canvas { position: relative; width: 1200px; height: 1000px; }
  .card {
    position: absolute;
    left: 265px;
    width: 666px;
    height: 397px;
    background: var(--card);
    box-shadow: 0 4px 14px var(--shadow);
  }
  .card--front { top: 73px; }
  .card--back { top: 532px; }

  .brand { position: absolute; text-align: center; white-space: nowrap; }
  .brand__name {
    display: block;
    font-weight: 400;
    color: var(--ink);
    line-height: 1;
  }
  .brand__tagline {
    display: block;
    color: var(--ink-soft);
    line-height: 1;
  }

  .card--front .brand { left: 46px; top: 160px; width: 252px; }
  .card--front .brand__name { font-size: 46px; }
  .card--front .brand__tagline { font-size: 20px; margin-top: 34px; }

  .card--back .brand { left: 180px; top: 148px; width: 306px; }
  .card--back .brand__name { font-size: 56px; }
  .card--back .brand__tagline { font-size: 24px; margin-top: 44px; }

  .contact { position: absolute; left: 374px; top: 124px; }
  .contact__name { font-size: 20px; line-height: 1; }
  .contact__role { font-size: 14px; margin-top: 7px; line-height: 1; }
  .contact__list { list-style: none; margin-top: 36px; }
  .contact__item {
    display: flex;
    align-items: center;
    gap: 6px;
    font-size: 15px;
    line-height: 19px;
  }
  .contact__icon { width: 10px; height: 10px; flex: none; }
</style>
</head>
<body>
<main class="canvas">
  <section class="card card--front">
    <div class="brand">
      <span class="brand__name">KRT Design</span>
      <span class="brand__tagline">Real Estate Investment</span>
    </div>
    <div class="contact">
      <p class="contact__name">Daniel Harper</p>
      <p class="contact__role">Founder</p>
      <ul class="contact__list">
        <li class="contact__item">
          <svg class="contact__icon" viewBox="0 0 10 10"><rect x="2.5" y="0.5" width="5" height="9" rx="1" fill="none" stroke="#2b2b2b" stroke-width="1"/></svg>
          + 1 404 555 0192
        </li>
        <li class="contact__item">
          <svg class="contact__icon" viewBox="0 0 10 10"><path d="M0.5 3.5 Q5 0 9.5 3.5 L8 4.5 L7 3 L3 3 L2 4.5 Z" fill="#2b2b2b"/><rect x="2" y="5" width="6" height="4" fill="#2b2b2b"/></svg>
          + 1 404 555 0148
        </li>
        <li class="contact__item">
          <svg class="contact__icon" viewBox="0 0 10 10"><rect x="0.5" y="2" width="9" height="6" fill="#2b2b2b"/><path d="M0.5 2 L5 5.5 L9.5 2" fill="none" stroke="#fff" stroke-width="0.8"/></svg>
          hello@krtdesignstudio.com
        </li>
        <li class="contact__item">
          <svg class="contact__icon" viewBox="0 0 10 10"><circle cx="5" cy="5" r="4.4" fill="none" stroke="#2b2b2b" stroke-width="1"/><ellipse cx="5" cy="5" rx="1.8" ry="4.4" fill="none" stroke="#2b2b2b" stroke-width="0.8"/><line x1="0.6" y1="5" x2="9.4" y2="5" stroke="#2b2b2b" stroke-width="0.8"/></svg>
          www.krtdesignstudio.com
        </li>
      </ul>
    </div>
  </section>

  <section class="card card--back">
    <div class="brand">
      <span class="brand__name">KRT Design</span>
      <span class="brand__tagline">Real Estate Investment</span>
    </div>
  </section>
</main>
</body>
</html>
```